Label for Green Tea extract tablets

I would like to get label designs for my green tea extract tablets. The bottle will be green probably (90%). 750 mg in each capsule, bottle will hold 120 tablets. people buying green tea are healthy aware and looking for something to help with aging, cancer, metabolism.
This is description which i have from manufacturer:
Green Tea is a powerful natural antioxidant and helps to maintain a healthy metabolism. It has been used in Chinese medicine for around 4,000 years. These tablets contain high quality green tea extract for maximum effect in one easy-to-take dose.
Some evidence suggests green tea may lower the chance of developing heart disease and certain types of cancer. It is also reported to increase the ratio of good (HDL) cholesterol to bad (LDL) cholesterol in the blood. Green Tea has also been claimed useful as a weight-loss aid by increasing your metabolic rate and by inducing thermogenesis.
I will add the logo soon.
I hope it helps a bit.
Thank you
Target Market(s)
All health carring adults
Colors
Designer to choose colors to be used in the design.
Requirements
Must have
- Green tea extract, as a name
- Manufacturer required details of the product
- Powerful antioxidant
- Digestive regulator
- Boosts immune system
- Regulated cholesterol in the blood
- Helps to fight cancer
- The safest dose to maximalise benefits
- Made in the UK with the flag
- Finest quality ingredients
- 120 capsules
- 750mg
- vegan
- vegetarian
Nice to have
- Nice picture, natural leaves, powder, tea tree plantation picture
Should not have
- Name of my company
- Considering downloaded file do not put any company name on the label, please

```html
<!DOCTYPE html>
<html lang="en">
<head>
<meta charset="utf-8">
<title>Leafwell Green Tea Label</title>
<link rel="stylesheet" href="https://fonts.googleapis.com/css2?family=Montserrat:wght@600;700&family=Questrial&display=swap">
<style>
:root{
  --page:#ffffff;
  --sky-top:#a9d6de;
  --sky-mid:#e4f1ee;
  --leaf-light:#b9d86a;
  --leaf-mid:#6fae2e;
  --leaf-deep:#2f7a1e;
  --panel-top:#4c9b2b;
  --panel-bottom:#c3d83a;
  --panel-right-top:#5aa22c;
  --panel-right-bottom:#d3df3a;
  --band:#1f6b22;
  --band-dark:#195a1c;
  --ink:#1d2a12;
  --ink-soft:#2e3b1d;
  --white:#ffffff;
  --brand:#5c6a55;
  --ring:#8cc63f;
  --tag:#3f7f3a;
}
*{margin:0;padding:0;box-sizing:border-box}
html,body{width:1200px;height:1000px;overflow:hidden;background:var(--page)}
body{position:relative;font-family:"Questrial",sans-serif;color:var(--ink)}
.label{position:absolute;left:443px;top:347px;width:734px;height:345px;overflow:hidden}
.label__scene{position:absolute;inset:0;background:linear-gradient(180deg,var(--sky-top) 0%,var(--sky-mid) 38%,var(--leaf-light) 55%,var(--leaf-mid) 75%,var(--leaf-deep) 100%)}
.panel{position:absolute;top:13px;width:176px;padding:8px 9px}
.panel--info{left:8px;height:308px;background:linear-gradient(180deg,var(--panel-top),var(--panel-bottom))}
.panel--nutrition{left:550px;height:330px;background:linear-gradient(180deg,var(--panel-right-top),var(--panel-right-bottom))}
.panel__title{font-family:"Montserrat",sans-serif;font-weight:700;font-size:11.5px;text-align:center;color:var(--ink);margin:-4px 0 6px}
.panel p{font-size:7.4px;line-height:1.3;text-align:justify;margin-bottom:6px}
.panel .fine{font-size:6.1px;line-height:1.3}
.nut{font-size:8px;line-height:1.3}
.nut strong{font-family:"Montserrat",sans-serif;font-weight:600}
.nut__row{display:flex;justify-content:space-between;text-decoration:underline;margin-top:10px}
.nut__small{font-size:6.6px;margin-top:10px}
.nut__allergen{position:absolute;left:9px;right:9px;top:254px;font-size:6.1px;line-height:1.3}
.brand{position:absolute;left:317px;top:28px;width:100px;height:100px;display:flex;align-items:center;justify-content:center}
.brand svg{position:absolute;inset:0}
.brand__name{position:relative;font-size:19px;letter-spacing:1px;color:var(--brand);text-align:center;line-height:1.15}
.tagline{position:absolute;left:190px;width:360px;top:152px;text-align:center;font-family:"Montserrat",sans-serif;font-weight:700;font-size:10px;letter-spacing:.6px;color:var(--tag)}
.benefits{position:absolute;left:290px;top:234px;width:153px;height:84px;background:var(--band);list-style:none;padding:3px 2px;text-align:center;color:var(--white);font-size:9.2px;line-height:1.3}
.band{position:absolute;left:0;right:0;top:321px;height:24px;background:var(--band-dark);color:var(--white)}
.band__faint{position:absolute;top:6px;font-size:6px;letter-spacing:2px;color:rgba(255,255,255,.45)}
.band__contact{left:28px}
.band__supp{left:584px}
.band__origin{position:absolute;left:296px;top:4px;font-size:11px;display:flex;align-items:center;gap:6px}
.band__count{position:absolute;left:474px;top:4px;font-size:11px}
.band__count b{font-family:"Montserrat",sans-serif;font-weight:700}
</style>
</head>
<body>
<section class="label">
  <div class="label__scene" role="img" aria-label="Soft sky above a green tea plantation with fresh tea leaves"></div>

  <div class="panel panel--info">
    <h2 class="panel__title">GREEN TEA</h2>
    <p>Green Tea is a powerful natural antioxidant and helps to maintain a healthy metabolism. It has been used in Chinese medicine for around 4,000 years. These tablets contain high quality green tea extract for maximum effect in one easy-to-take dose.</p>
    <p>Evidence suggests green tea may lower the chance of developing heart disease. It is also reported to increase the ratio of good (HDL) cholesterol to bad (LDL) cholesterol in the blood. Green Tea has also been claimed useful as a weight-loss aid by increasing your metabolic rate and by inducing thermogenesis.</p>
    <p>SUGGESTED USE: Take 1 tablet per day with food.</p>
    <p class="fine">DISCLAIMER: this product is not categorised as a herbal medicine, it is sold as a food supplement. The statement contained on this label does not imply that this product has any medicinal properties, use or efficacy. This product should not be used as a substitute for a varied and balanced diet and do not exceed recommended daily dose. Store in a cool dry place and keep out of reach of children.</p>
  </div>

  <div class="brand">
    <svg viewBox="0 0 100 100" aria-hidden="true"><circle cx="50" cy="50" r="47" fill="none" stroke="var(--ring)" stroke-width="2.5"/></svg>
    <span class="brand__name">Leafwell</span>
  </div>
  <h1 class="tagline">HELPS MAINTAIN A HEALTHY METABOLISM</h1>

  <ul class="benefits">
    <li>Powerful antioxidant</li>
    <li>Digestive regulator</li>
    <li>Boosts immune system</li>
    <li>Regulated cholesterol in the blood</li>
    <li>Helps to fight cancer</li>
    <li>The safest dose to maximalise benefits</li>
  </ul>

  <div class="panel panel--nutrition">
    <h2 class="panel__title">NUTRITIONAL INFO</h2>
    <div class="nut">
      <div><strong>Serving Size:</strong> 1 Tablet</div>
      <div><strong>Servings per container:</strong> 120</div>
      <div class="nut__row"><span>Active Ingredients</span><strong>Per Tablet</strong></div>
      <div>Green Tea &nbsp;750mg</div>
      <div class="nut__small">Inactive Ingredients:<br>Microcrystaline Cellulose, Silicon Dioxide, Magnesium Stearate.</div>
    </div>
    <p class="nut__allergen">ALLERGEN WARNING: This product is manufactured on equipment which processes products containing nuts, milk, gluten, egg, soya and peanuts.</p>
  </div>

  <div class="band">
    <span class="band__faint band__contact">CONTACT INFORMATION</span>
    <span class="band__origin">Made in the UK
      <svg width="22" height="12" viewBox="0 0 60 30" aria-label="UK flag" role="img">
        <rect width="60" height="30" fill="#012169"/>
        <path d="M0,0 60,30 M60,0 0,30" stroke="#fff" stroke-width="6"/>
        <path d="M0,0 60,30 M60,0 0,30" stroke="#C8102E" stroke-width="2"/>
        <path d="M30,0V30M0,15H60" stroke="#fff" stroke-width="10"/>
        <path d="M30,0V30M0,15H60" stroke="#C8102E" stroke-width="6"/>
      </svg>
    </span>
    <span class="band__count"><b>120</b>TABLETS</span>
    <span class="band__faint band__supp">FOOD SUPPLEMENT</span>
  </div>
</section>
</body>
</html>
```